Flyer-Design für Unternehmen mit Fokus auf 3D-Messtechnik
Zielgruppe
Deutsch:
Wir sind ein Ingenieur Dienstleistungsunternehmen mit Fokus auf 3D-Messtechnik und zerstörungsfreier Prüftechnik mit kamerabasierten Systemen. Wir entwickeln Prüfalgorithmen zur automatisierten Bauteilinspektion.
Unsere Zielgruppe sind produzierende Unternehmen die ihre Qualitätskontrolle durch optische Prüfsysteme ergänzen und/oder komplexe Bauteilmessungen bei einem Dienstleister outsourcen möchten.
Englisch:
We are an engineering service company with focus on 3D measurement and non destructive testing with camera systems. We develop inspection algorithms regarding automated quality check of components. Our target group are producing companies which want to perform there quality checks by optical inspection systems and/or want to have high precise measurements of there parts.
Aufgabenstellung
The flyer should give a good overview of the companies services. The format can be 6 pages and high side but you can also be creative if another format matches well. The different business areas are:
1. 3D-Messtechnik
2. Zerstörungsfreie Prüftechnik mit bildgebenden Systemen
3. Softwareentwicklung mit Schwerpunkt optische Qualitätskontrolle
4. Machbarkeitsstudien
5. Schulungen
A first draft of content i have uploaded in a word document, please just insert it i can edit it later.
To every of the 5 business areas suggestions of pictures can be made, also from stock pictures. I will have a look in parallel.

```html
<!DOCTYPE html>
<html lang="de">
<head>
<meta charset="utf-8">
<title>Optimess Werk – Flyer</title>
<link href="https://fonts.googleapis.com/css2?family=Open+Sans:wght@400;600;700;800&display=swap" rel="stylesheet">
<style>
  :root {
    --navy: #1d3b6b;
    --navy-deep: #16305a;
    --ink: #2d2d2d;
    --paper: #ffffff;
    --stage: #f1f2f4;
    --photo-blue-a: #3e5f93;
    --photo-blue-b: #243f6e;
    --photo-warm-a: #c9a27a;
    --photo-warm-b: #5f6f86;
  }
  * { box-sizing: border-box; margin: 0; padding: 0; }
  html, body { width: 981px; height: 1200px; overflow: hidden; }
  body {
    background: var(--stage);
    font-family: "Open Sans", Arial, sans-serif;
    color: var(--ink);
    position: relative;
  }
  .spread {
    position: absolute;
    left: 40px;
    width: 900px;
    height: 310px;
    background: var(--paper);
    box-shadow: 0 6px 18px rgba(0,0,0,.12);
  }
  .spread--outside { top: 50px; }
  .spread--inside { top: 410px; }
  .panel {
    position: absolute;
    top: 0;
    height: 310px;
    overflow: hidden;
    background: var(--paper);
  }
  .single {
    top: 810px;
    width: 300px;
    box-shadow: 0 6px 18px rgba(0,0,0,.12);
  }
  .single--cover { left: 160px; }
  .single--back { left: 520px; }

  .headline {
    font-weight: 800;
    text-transform: uppercase;
    color: var(--navy);
    font-size: 20px;
    line-height: 1.02;
    letter-spacing: .3px;
  }
  .body-copy {
    font-size: 8px;
    line-height: 1.3;
    color: var(--ink);
  }

  .photo { position: absolute; }
  .photo--tech {
    background: linear-gradient(160deg, var(--photo-blue-a), var(--photo-blue-b));
  }
  .photo--workshop {
    background: radial-gradient(circle at 35% 35%, var(--photo-warm-a), var(--photo-warm-b) 70%, #3b4e6c);
  }
  .photo--machine {
    background: linear-gradient(180deg, #5a79a8, #2f4d7d 60%, #27426f);
  }
  .photo--machine-dark {
    background: linear-gradient(180deg, #4a6a9c, #2a4674);
  }

  /* Software panel */
  .software-copy { position: absolute; left: 120px; top: 0; width: 180px; padding: 28px 16px 0 20px; }
  .software-copy .body-copy { margin-top: 16px; }

  /* Training / contact panel */
  .training-copy { position: absolute; left: 0; top: 0; width: 100%; padding: 34px 28px 0 34px; }
  .training-copy .body-copy { margin-top: 16px; font-size: 8.2px; }
  .contact-band {
    position: absolute; left: 0; bottom: 0; width: 100%; height: 108px;
    background: var(--navy);
    color: #fff; text-align: center;
    padding-top: 34px;
    font-size: 7.6px; line-height: 1.45;
  }
  .contact-band strong { font-weight: 700; display: block; }
  .icon-badge {
    position: absolute; width: 48px; height: 48px; border-radius: 50%;
    background: #fff; border: 2px solid var(--navy);
    display: flex; align-items: center; justify-content: center;
  }
  .contact-band .icon-badge { left: 126px; top: -24px; }

  /* Cover */
  .cover-brand {
    position: absolute; left: 0; top: 0; width: 100%; height: 210px;
    display: flex; flex-direction: column; align-items: center; justify-content: center; gap: 12px;
  }
  .brand-square { width: 44px; height: 44px; border-radius: 8px; background: #fff; }
  .brand-name { color: #fff; font-weight: 600; font-size: 24px; letter-spacing: 1.5px; }
  .cover-band {
    position: absolute; left: 0; bottom: 0; width: 100%; height: 96px;
    background: var(--navy); border-top: 3px solid #fff;
    color: #fff; padding: 20px 24px 0;
  }
  .cover-band h2 { font-size: 13px; font-weight: 800; text-transform: uppercase; letter-spacing: .3px; }
  .cover-band p { font-size: 8.2px; margin-top: 8px; line-height: 1.3; }

  /* Messtechnik panel */
  .measure-copy { position: absolute; left: 0; top: 0; width: 100%; padding: 24px 22px 0 26px; }
  .measure-copy .body-copy { margin-top: 12px; }
  .measure-photo { left: 0; top: 160px; width: 100%; height: 150px; opacity: .95; }
  .measure-photo::after {
    content: ""; position: absolute; inset: 0; background: rgba(29,59,107,.55);
  }
  .measure-photo .icon-badge { left: 126px; top: -8px; z-index: 2; }
  .express-box {
    position: absolute; left: 36px; top: 24px; width: 228px; height: 108px;
    border: 1px solid rgba(255,255,255,.85); z-index: 1;
    color: #fff; text-align: center; padding: 34px 14px 0;
  }
  .express-box h3 { font-size: 11px; font-weight: 700; text-transform: uppercase; letter-spacing: .3px; }
  .express-box p { font-size: 7.8px; line-height: 1.3; margin-top: 8px; }

  .ndt-copy { position: absolute; left: 300px; top: 0; width: 222px; padding: 26px 16px 0 24px; }
  .ndt-copy .body-copy { margin-top: 14px; }
  .study-copy { position: absolute; left: 738px; top: 0; width: 162px; padding: 30px 12px 0 16px; }
  .study-copy .body-copy { margin-top: 14px; font-size: 7.6px; }

  .fold { position: absolute; top: 0; width: 1px; height: 100%; background: rgba(0,0,0,.06); }
</style>
</head>
<body>

<!-- Outside spread -->
<section class="spread spread--outside">
  <div class="panel" style="left:0;width:300px;">
    <div class="photo photo--tech" style="left:0;top:0;width:120px;height:310px;" role="img" aria-label="Foto: Hand an einer Tastatur mit Binärcode-Überlagerung in Blautönen"></div>
    <div class="software-copy">
      <h2 class="headline">Software-<br>entwick-<br>lung</h2>
      <p class="body-copy">Wir entwickeln Software mit Fokus auf Computer Vision Applikationen. Dazu verwenden wir eine geschwindigkeitsoptimierte Bildverarbeitungsbibliothek kombiniert mit selbst entwickelten Algorithmen. Die Kameraanbindung sowie Beleuchtungsansteuerung erfolgen in der hauseigenen Software, sie erhalten also die Computer Vision Funktionalität aus einer Hand.</p>
    </div>
  </div>

  <div class="panel" style="left:300px;width:300px;">
    <div class="training-copy">
      <h2 class="headline">Schulung und<br>Beratung</h2>
      <p class="body-copy">Benötigen Sie Unterstützung bei der Programmierung Ihrer Kalvora Messmaschine unter MeasPro oder im Bereich der digitalen Bildverarbeitung? Kontaktieren Sie uns und wir besprechen die weitere Vorgehensweise um Sie optimal zu unterstützen.</p>
    </div>
    <div class="contact-band">
      <div class="icon-badge">
        <svg width="28" height="28" viewBox="0 0 28 28" fill="none" stroke="#1d3b6b" stroke-width="1.4" stroke-linejoin="round">
          <path d="M5 9c-1 4 2 10 7 13l2-3-3-3-2 1c-1-2-2-4-2-5l2-1-1-4z"/>
          <rect x="12" y="5" width="12" height="9"/>
          <path d="M12 5l6 5 6-5"/>
        </svg>
      </div>
      OPTIMESS WERK GbR • Lindenhofweg 12-14 • 58000 Musterstadt
      <strong>IHR ANSPRECHPARTNER:</strong>
      Dr.-Ing. Jonas Verhagen • info@optimess-werk.de • Tel: +49 151 000 000 00<br>
      www.optimess-werk.de
    </div>
  </div>

  <div class="panel" style="left:600px;width:300px;">
    <div class="photo photo--workshop" style="left:0;top:0;width:300px;height:214px;" role="img" aria-label="Foto: unscharfe Werkstatt mit Person im Hintergrund"></div>
    <div class="cover-brand">
      <div class="brand-square"></div>
      <div class="brand-name">OPTIMESS WERK</div>
    </div>
    <div class="cover-band">
      <h2>Ihr kompetenter Partner.</h2>
      <p>Im Bereich 3D-Messtechnik und<br>der zerstörungsfreien Prüftechnik.</p>
    </div>
  </div>
  <div class="fold" style="left:300px"></div>
  <div class="fold" style="left:600px"></div>
</section>

<!-- Inside spread -->
<section class="spread spread--inside">
  <div class="panel" style="left:0;width:300px;">
    <div class="measure-copy">
      <h2 class="headline">Messtechnik</h2>
      <p class="body-copy">Wir vermessen Ihre Bauteile entsprechend Ihren Anforderungen mit modernen Messmaschinen entweder optisch, taktil oder in Kombination der beiden Verfahren. Die Messungen werden ausschließlich in einem klimatisierten Messraum vorgenommen. Der Messbericht kann in verschiedenen Formaten z.B. als Text,- CSV,- oder Exceldatei geliefert werden und ist natürlich entsprechend Ihren Anforderungen formatierbar.</p>
    </div>
    <div class="photo photo--machine measure-photo" role="img" aria-label="Foto: Koordinatenmessmaschine mit Messtaster, blau eingefärbt">
      <div class="icon-badge">
        <svg width="28" height="28" viewBox="0 0 28 28" fill="none" stroke="#1d3b6b" stroke-width="1.4" stroke-linejoin="round" stroke-linecap="round">
          <path d="M22 6c-5 0-9 3-11 8l3 3c5-2 8-6 8-11z"/>
          <circle cx="17.5" cy="10.5" r="1.6"/>
          <path d="M11 14l-4 1 2 2M14 17l-1 4-2-2"/>
          <path d="M9 19l-4 4M7 17l-3 3M11 21l-3 3"/>
        </svg>
      </div>
      <div class="express-box">
        <h3>Express-Service</h3>
        <p>Benötigen Sie schnell Ihre Messergebnisse rufen Sie uns an, wir vereinbaren umgehend einen Termin um Ihre Bauteile abzuholen.</p>
      </div>
    </div>
  </div>

  <div class="ndt-copy">
    <h2 class="headline">Zerstörungs-<br>freie<br>Prüftechnik</h2>
    <p class="body-copy">Sind Sie an einem Inspektionssystem zur optischen Qualitätskontrolle Ihrer Bauteile interessiert? Wir entwickeln das System entsprechend Ihren Anforderungen, von einem manuellen Inspektionsarbeitsplatz bis hin zu einer automatisierten Defekterkennung. Mit Hilfe unserer umfangreichen Computer Vision Bibliothek erhalten Sie modernste Bildverarbeitungsfunktionen.</p>
  </div>

  <div class="photo photo--machine-dark" style="left:522px;top:0;width:216px;height:310px;" role="img" aria-label="Foto: Fräsmaschine mit Werkzeugspindel über einem Werkstück, blau eingefärbt"></div>

  <div class="study-copy">
    <h2 class="headline">Machbar-<br>keits-<br>studien</h2>
    <p class="body-copy">Haben Sie ein Automatisierungsvorhaben im Fokus aber möchten zunächst herausarbeiten welche Computer Vision Technologien am besten für das Projekt geeignet sind? Mit welchem zeitlichen Umfang und Budget zu rechnen ist? Wie prozesssicher kann eine automatische Bildauswertung für das Projekt eingeordnet werden? Gerne führen wir eine Studie für Sie durch, dafür stehen unterschiedliche Kameras, Objektive, Filter und Beleuchtungsmodule zur Verfügung.</p>
  </div>
  <div class="fold" style="left:300px"></div>
  <div class="fold" style="left:600px"></div>
</section>

<!-- Front cover single -->
<section class="panel single single--cover">
  <div class="photo photo--workshop" style="left:0;top:0;width:300px;height:214px;" role="img" aria-label="Foto: unscharfe Werkstatt mit Person im Hintergrund"></div>
  <div class="cover-brand">
    <div class="brand-square"></div>
    <div class="brand-name">OPTIMESS WERK</div>
  </div>
  <div class="cover-band">
    <h2>Ihr kompetenter Partner.</h2>
    <p>Im Bereich 3D-Messtechnik und<br>der zerstörungsfreien Prüftechnik.</p>
  </div>
</section>

<!-- Back single -->
<section class="panel single single--back">
  <div class="training-copy">
    <h2 class="headline">Schulung und<br>Beratung</h2>
    <p class="body-copy">Benötigen Sie Unterstützung bei der Programmierung Ihrer Kalvora Messmaschine unter MeasPro oder im Bereich der digitalen Bildverarbeitung? Kontaktieren Sie uns und wir besprechen die weitere Vorgehensweise um Sie optimal zu unterstützen.</p>
  </div>
  <div class="contact-band">
    <div class="icon-badge">
      <svg width="28" height="28" viewBox="0 0 28 28" fill="none" stroke="#1d3b6b" stroke-width="1.4" stroke-linejoin="round">
        <path d="M5 9c-1 4 2 10 7 13l2-3-3-3-2 1c-1-2-2-4-2-5l2-1-1-4z"/>
        <rect x="12" y="5" width="12" height="9"/>
        <path d="M12 5l6 5 6-5"/>
      </svg>
    </div>
    OPTIMESS WERK GbR • Lindenhofweg 12-14 • 58000 Musterstadt
    <strong>IHR ANSPRECHPARTNER:</strong>
    Dr.-Ing. Jonas Verhagen • info@optimess-werk.de • Tel: +49 151 000 000 00<br>
    www.optimess-werk.de
  </div>
</section>

</body>
</html>
```